Business Card Design

I need a business card design for a photography business that specializes in headshots and portraits.

Target Market(s)

Business professionals, actors, actresses

Industry/Entity Type

Business

Contact Information for Business Card

Cobalt Ridge Photography, Greg Whitlow, 5817 Kellerman Ave, Suite 416, Fort Wayne, IN 46915, 260.555.0187, www.cobaltridgephoto.example. greg.whitlow@cobaltridgephoto.example

Requirements
Must have
• The business card should state the type of photography services offered: headshots and portraits.

```html
<!DOCTYPE html>
<html lang="en">
<head>
<meta charset="utf-8">
<title>Cobalt Ridge Photography – Business Card</title>
<link rel="stylesheet" href="https://fonts.googleapis.com/css2?family=Lato:wght@700;900&display=swap">
<style>
  :root {
    --page-bg: #ffffff;
    --card-bg: #000000;
    --text: #ffffff;
    --accent-teal: #3fb8d4;
    --accent-magenta: #e0287a;
    --accent-violet: #6a2a8c;
  }
  html, body {
    margin: 0;
    padding: 0;
    width: 1200px;
    height: 900px;
    overflow: hidden;
    background: var(--page-bg);
  }
  .canvas {
    position: relative;
    width: 1200px;
    height: 900px;
  }
  .card {
    position: absolute;
    left: 147px;
    top: 190px;
    width: 911px;
    height: 522px;
    background: var(--card-bg);
    color: var(--text);
    font-family: "Lato", sans-serif;
    overflow: hidden;
  }
  .card-title {
    position: absolute;
    left: 0;
    right: 0;
    top: 52px;
    margin: 0;
    text-align: center;
    font-weight: 900;
    font-size: 44px;
    letter-spacing: -0.5px;
    transform: translateX(-4px) scaleX(0.8);
  }
  .card-services {
    position: absolute;
    left: 0;
    right: 0;
    top: 110px;
    margin: 0;
    text-align: center;
    font-weight: 700;
    font-size: 17px;
    letter-spacing: 4px;
    color: var(--accent-teal);
    transform: translateX(-4px);
  }
  .camera-art {
    position: absolute;
    left: 45px;
    top: 160px;
    width: 420px;
    height: 320px;
  }
  .contact {
    position: absolute;
    left: 490px;
    top: 290px;
    margin: 0;
    font-weight: 700;
    font-size: 20.5px;
    line-height: 32px;
    white-space: nowrap;
  }
  .contact-line { display: block; }
</style>
</head>
<body>
<div class="canvas">
  <section class="card">
    <h1 class="card-title">PHOTOGRAPHY BUSINESS</h1>
    <p class="card-services">HEADSHOTS &amp; PORTRAITS</p>

    <svg class="camera-art" role="img" aria-label="Illustration of a compact camera with swirling teal and magenta light splashes and butterflies" viewBox="0 0 420 320">
      <defs>
        <radialGradient id="glow-teal" cx="0.3" cy="0.35" r="0.5">
          <stop offset="0" stop-color="#3fb8d4" stop-opacity="0.75"/>
          <stop offset="1" stop-color="#3fb8d4" stop-opacity="0"/>
        </radialGradient>
        <radialGradient id="glow-magenta" cx="0.65" cy="0.65" r="0.45">
          <stop offset="0" stop-color="#e0287a" stop-opacity="0.8"/>
          <stop offset="1" stop-color="#e0287a" stop-opacity="0"/>
        </radialGradient>
        <radialGradient id="glow-violet" cx="0.55" cy="0.3" r="0.3">
          <stop offset="0" stop-color="#6a2a8c" stop-opacity="0.6"/>
          <stop offset="1" stop-color="#6a2a8c" stop-opacity="0"/>
        </radialGradient>
      </defs>
      <rect width="420" height="320" fill="url(#glow-teal)"/>
      <rect width="420" height="320" fill="url(#glow-violet)"/>
      <rect width="420" height="320" fill="url(#glow-magenta)"/>
    </svg>

    <p class="contact">
      <span class="contact-line">Cobalt Ridge : Photography</span>
      <span class="contact-line">Greg Whitlow : 5817 Kellerman Ave,</span>
      <span class="contact-line">Suite 416, Fort Wayne, IN 46915,</span>
      <span class="contact-line">Phone : 260.555.0187</span>
      <span class="contact-line">www.cobaltridgephoto.example</span>
      <span class="contact-line">greg.whitlow@cobaltridgephoto.example</span>
    </p>
  </section>
</div>
</body>
</html>
```